Letterhead designs for Property Management firm

Would like to see some different letterhead/envelope designs We are a residential property management company. We would like to see designs that utilize blue/grays/black

```html
<!DOCTYPE html>
<html lang="en">
<head>
<meta charset="utf-8">
<title>Harborview Property Management – Envelope</title>
<link href="https://fonts.googleapis.com/css2?family=Arimo:wght@400;700&family=Exo+2:wght@400&display=swap" rel="stylesheet">
<style>
  :root {
    --brand-blue: #0354a6;
    --ink: #111111;
    --outline: #1a1a1a;
    --paper: #ffffff;
    --sketch-light: #eef0f2;
    --sketch-mid: #d4d7db;
  }
  html, body {
    margin: 0;
    padding: 0;
    width: 1200px;
    height: 1200px;
    overflow: hidden;
    background: var(--paper);
  }
  .canvas {
    position: relative;
    width: 1200px;
    height: 1200px;
  }
  .envelope-shape {
    position: absolute;
    left: 0;
    top: 0;
  }
  .brand {
    position: absolute;
    left: 132px;
    top: 486px;
    display: flex;
    align-items: center;
    gap: 10px;
  }
  .brand-mark {
    width: 22px;
    height: 22px;
    background: var(--brand-blue);
  }
  .brand-name {
    font-family: "Arimo", Arial, sans-serif;
    font-weight: 700;
    font-size: 19px;
    line-height: 1.15;
    color: var(--brand-blue);
    letter-spacing: 0.5px;
  }
  .tagline {
    position: absolute;
    left: 682px;
    top: 472px;
    font-family: "Exo 2", sans-serif;
    font-size: 19px;
    letter-spacing: 1.3px;
    color: var(--ink);
  }
  .skyline-art {
    position: absolute;
    left: 688px;
    top: 680px;
    width: 376px;
    height: 158px;
    background: linear-gradient(180deg, var(--paper) 0%, var(--sketch-light) 35%, var(--sketch-mid) 100%);
  }
  .contact-list {
    position: absolute;
    left: 131px;
    top: 711px;
    margin: 0;
    padding: 0;
    list-style: none;
    font-family: "Arimo", Arial, sans-serif;
    font-size: 15px;
    color: var(--ink);
  }
  .contact-item {
    display: flex;
    align-items: center;
    gap: 8px;
    height: 30px;
    margin-bottom: 6px;
  }
  .contact-item.address {
    line-height: 15px;
  }
  .contact-icon {
    flex: none;
    width: 30px;
    height: 30px;
  }
</style>
</head>
<body>
<main class="canvas">

  <svg class="envelope-shape" width="1200" height="1200" viewBox="0 0 1200 1200">
    <rect class="envelope-body" x="90" y="420" width="1020" height="469" fill="var(--paper)" stroke="#555" stroke-width="1"/>
    <path class="envelope-flap" d="M90,420 L108,350 Q120,311 155,311 L1045,311 Q1080,311 1092,350 L1110,420 Z" fill="var(--brand-blue)" stroke="var(--outline)" stroke-width="1.2"/>
    <g class="frame-line" fill="var(--brand-blue)">
      <polyline points="669,470 1078,470 1078,840 372,840" fill="none" stroke="var(--brand-blue)" stroke-width="3"/>
      <circle cx="669" cy="470" r="7"/>
      <circle cx="372" cy="840" r="7"/>
    </g>
  </svg>

  <div class="brand">
    <span class="brand-mark"></span>
    <span class="brand-name">HARBORVIEW<br>PROPERTY MANAGEMENT</span>
  </div>

  <div class="tagline">Your Full Service Real Estate Company</div>

  <div class="skyline-art" role="img" aria-label="Light pencil sketch of a city skyline with office towers"></div>

  <ul class="contact-list">
    <li class="contact-item">
      <svg class="contact-icon" viewBox="0 0 30 30">
        <circle cx="15" cy="15" r="15" fill="var(--brand-blue)"/>
        <g fill="none" stroke="#fff" stroke-width="1.3">
          <circle cx="15" cy="15" r="8"/>
          <ellipse cx="15" cy="15" rx="3.5" ry="8"/>
          <line x1="7" y1="15" x2="23" y2="15"/>
          <path d="M8.5,11 H21.5 M8.5,19 H21.5"/>
        </g>
      </svg>
      <span>www.harborview-homes.com</span>
    </li>
    <li class="contact-item">
      <svg class="contact-icon" viewBox="0 0 30 30">
        <circle cx="15" cy="15" r="15" fill="var(--brand-blue)"/>
        <g fill="none" stroke="#fff" stroke-width="1.3">
          <rect x="7.5" y="10" width="15" height="10"/>
          <polyline points="7.5,10 15,16 22.5,10"/>
          <path d="M7.5,20 L12.5,15.5 M22.5,20 L17.5,15.5"/>
        </g>
      </svg>
      <span>office@harborview-homes.com</span>
    </li>
    <li class="contact-item">
      <svg class="contact-icon" viewBox="0 0 30 30">
        <circle cx="15" cy="15" r="15" fill="var(--brand-blue)"/>
        <circle cx="15" cy="15" r="10" fill="none" stroke="#fff" stroke-width="1.3"/>
        <path d="M11,9.5 L13,9.5 L14,12.5 L12.6,13.6 Q14,16.4 16.4,17.4 L17.5,16 L20.5,17 L20.5,19 Q19.5,20.5 17.5,20.2 Q11.5,18.5 9.8,12.5 Q9.5,10.5 11,9.5 Z" fill="#fff"/>
      </svg>
      <span>+1 555-014-2280</span>
    </li>
    <li class="contact-item address">
      <svg class="contact-icon" viewBox="0 0 30 30">
        <circle cx="15" cy="15" r="15" fill="var(--brand-blue)"/>
        <path d="M15,24 C11,18.5 9.5,15.5 9.5,12.5 A5.5,5.5 0 0 1 20.5,12.5 C20.5,15.5 19,18.5 15,24 Z" fill="#fff"/>
        <circle cx="15" cy="12.5" r="2.2" fill="var(--brand-blue)"/>
      </svg>
      <span>2480 Maple Grove Ave<br>91820 Fairview, California</span>
    </li>
  </ul>

</main>
</body>
</html>
```